KPV Construction we build lodges in Botswana

We need a Design Layout only with Categories where we can update each projects photos.... We have a web address and a host - kpv.construction

```html
<!DOCTYPE html>
<html lang="en">
<head>
<meta charset="utf-8">
<title>KPV Construction</title>
<link href="https://fonts.googleapis.com/css2?family=Montserrat:wght@400;500;600;700&family=Poppins:wght@400;500;600&display=swap" rel="stylesheet">
<style>
:root{
  --red:#ee1c25;
  --ink:#111111;
  --text:#555555;
  --muted:#8a8a8a;
  --white:#ffffff;
  --black:#0b0b0b;
  --card:#f7f7f7;
  --star:#f58a1f;
}
*{margin:0;padding:0;box-sizing:border-box}
html,body{width:1200px;height:3758px;overflow:hidden;background:var(--white)}
body{position:relative;font-family:"Poppins",sans-serif;color:var(--ink)}
.abs{position:absolute}
.btn{position:absolute;background:var(--red);color:var(--white);font-family:"Montserrat",sans-serif;font-weight:600;display:flex;align-items:center;justify-content:center}
/* header */
.site-header{position:absolute;left:0;top:0;width:1200px;height:96px;border-bottom:3px solid var(--red);background:var(--white)}
.brand{position:absolute;left:110px;top:26px;font-family:"Montserrat",sans-serif;font-weight:500;font-size:32px;color:var(--red)}
.nav{position:absolute;left:606px;top:36px;display:flex;gap:34px;font-family:"Montserrat",sans-serif;font-size:16px;font-weight:500}
.nav a{color:var(--ink);text-decoration:none}
.nav a.active{color:var(--red)}
/* hero */
.hero{position:absolute;left:0;top:96px;width:1200px;height:650px}
.hero-title{position:absolute;left:0;top:186px;width:1200px;text-align:center;font-family:"Montserrat",sans-serif;font-weight:600;font-size:72px;line-height:90px;color:var(--white);letter-spacing:-1px}
.hero-sub{position:absolute;left:0;top:282px;width:1200px;text-align:center;font-family:"Montserrat",sans-serif;font-weight:500;font-size:21px;line-height:34px;color:var(--white)}
.hero-dots .dot{position:absolute;border-radius:50%;background:var(--white)}
/* section heads */
.section-title{position:absolute;left:0;width:1200px;text-align:center;font-family:"Montserrat",sans-serif;font-weight:600;font-size:52px;color:var(--ink)}
/* about */
.frame{position:absolute;background:var(--white);padding:7px;box-shadow:0 4px 14px rgba(0,0,0,.25)}
.frame div{width:100%;height:100%}
.about-title{position:absolute;left:665px;top:902px;font-family:"Montserrat",sans-serif;font-weight:600;font-size:52px}
.about-text{position:absolute;left:670px;top:990px;width:416px;font-family:"Montserrat",sans-serif;font-size:15px;line-height:27px;color:var(--text);text-align:justify}
/* projects */
.project{position:absolute;width:309px;height:192px}
/* news */
.news-card{position:absolute;background:var(--white);box-shadow:0 2px 12px rgba(0,0,0,.2);padding:10px}
.news-card div{width:100%;height:100%}
.news-heading{position:absolute;left:678px;top:2252px;font-family:"Montserrat",sans-serif;font-weight:600;font-size:26px}
.news-text{position:absolute;left:678px;top:2300px;width:400px;font-family:"Montserrat",sans-serif;font-size:14px;line-height:26px;color:var(--muted)}
.arrow{position:absolute;width:26px;height:26px}
/* testimonials */
.quote{position:absolute;top:2880px;width:295px;height:175px;background:var(--card);border-radius:8px;box-shadow:0 3px 14px rgba(0,0,0,.18);padding:52px 24px 0;text-align:center;font-family:"Montserrat",sans-serif;font-size:13px;line-height:24px;color:var(--text)}
.quote::after{content:"";position:absolute;left:50%;bottom:-12px;margin-left:-12px;border-left:12px solid transparent;border-right:12px solid transparent;border-top:12px solid var(--card)}
.avatar{position:absolute;top:2834px;width:86px;height:86px;border-radius:50%;border:3px solid var(--white);box-shadow:0 2px 8px rgba(0,0,0,.2)}
.person{position:absolute;top:3102px;width:295px;text-align:center;font-family:"Montserrat",sans-serif}
.person .name{color:var(--red);font-weight:500;font-size:19px}
.person .place{color:var(--ink);font-size:15px;margin-top:4px}
.person .stars{color:var(--star);font-size:17px;letter-spacing:3px;margin-top:4px}
/* footer */
.footer{position:absolute;left:0;top:3300px;width:1200px;height:458px}
.footer-brand{position:absolute;left:112px;top:3468px;font-family:"Montserrat",sans-serif;font-weight:500;font-size:38px;line-height:46px;color:var(--white)}
.f-head{position:absolute;top:3436px;font-family:"Montserrat",sans-serif;font-weight:500;font-size:20px;color:var(--white)}
.f-text{position:absolute;font-family:"Montserrat",sans-serif;font-size:12px;line-height:20px;color:var(--white)}
.f-links{position:absolute;left:696px;top:3478px;list-style:none;font-family:"Montserrat",sans-serif;font-size:13px;line-height:27px;color:var(--white)}
.social{position:absolute;top:3698px;width:18px;height:18px;border-radius:50%;background:#3a3a3a}
.social.on{background:var(--red);width:24px;height:24px;top:3695px}
</style>
</head>
<body>

<header class="site-header">
  <div class="brand">KPV Construction</div>
  <nav class="nav">
    <a class="active" href="#">Home</a><a href="#">About Us</a><a href="#">Projects</a><a href="#">Testimonials</a><a href="#">Contact</a>
  </nav>
</header>

<section class="hero">
  <svg width="1200" height="650" class="abs" style="left:0;top:0" role="img" aria-label="Photo of a timber lodge with a deck beside a lake among trees">
    <defs>
      <linearGradient id="heroGrad" x1="0" y1="0" x2="1" y2="1">
        <stop offset="0" stop-color="#8a9a6a"/>
        <stop offset=".45" stop-color="#4f6a32"/>
        <stop offset="1" stop-color="#2f4a1f"/>
      </linearGradient>
    </defs>
    <polygon points="0,0 1200,0 1200,574 870,642 0,560" fill="url(#heroGrad)"/>
    <polyline points="0,560 870,642 1200,574" fill="none" stroke="var(--red)" stroke-width="3"/>
  </svg>
  <h1 class="hero-title">KPV CONSTRUCTION</h1>
  <p class="hero-sub">Lorem ipsum dolor sit amet, consectetur adipiscing elit,sed<br>do eiusmod tempor incididunt</p>
  <div class="btn" style="left:523px;top:372px;width:152px;height:42px;font-size:16px">Read More</div>
  <div class="hero-dots">
    <div class="dot" style="left:1127px;top:276px;width:26px;height:26px;background:none;border:3px solid var(--white)"></div>
    <div class="dot" style="left:1134px;top:283px;width:12px;height:12px"></div>
    <div class="dot" style="left:1134px;top:320px;width:12px;height:12px"></div>
    <div class="dot" style="left:1134px;top:347px;width:12px;height:12px"></div>
  </div>
</section>

<section class="about">
  <div class="frame" style="left:264px;top:838px;width:220px;height:265px"><div role="img" aria-label="Lodge interior with timber walls" style="background:linear-gradient(160deg,#6d5a3a,#3b3020)"></div></div>
  <div class="frame" style="left:330px;top:965px;width:240px;height:340px"><div role="img" aria-label="Stone path leading to timber cabins" style="background:linear-gradient(170deg,#9cc2e0,#6f8a4a 55%,#4e6a2e)"></div></div>
  <div class="frame" style="left:170px;top:1165px;width:240px;height:200px"><div role="img" aria-label="Tented lodge at sunset" style="background:linear-gradient(180deg,#c7806a,#5b3b3a)"></div></div>
  <div class="frame" style="left:110px;top:922px;width:257px;height:252px"><div role="img" aria-label="Treehouse lodge in lush forest" style="background:linear-gradient(160deg,#6f9a3e,#2e4a1e)"></div></div>
  <h2 class="about-title">About Us</h2>
  <p class="about-text">Sed ut perspiciatis unde omnis iste natus error sit voluptatem accusantium doloremque laudantium, totam rem aperiam, eaque ipsa quae ab illo inventore veritatis et quasi architecto beatae vitae dicta sunt explicabo. Nemo enim ipsam voluptatem quia voluptas sit aspernatur aut odit aut fugit, sed quia consequuntur magni dolores eos qui ratione voluptatem sequi nesciunt.</p>
  <div class="btn" style="left:670px;top:1250px;width:186px;height:52px;font-size:17px">Read More</div>
</section>

<section class="projects">
  <h2 class="section-title" style="top:1476px">Projects</h2>
  <div class="project" role="img" aria-label="Thatched lodge among trees" style="left:112px;top:1585px;background:linear-gradient(170deg,#a9c0d8,#6a7a4a 55%,#4a4a30)"></div>
  <div class="project" role="img" aria-label="Thatched veranda lodge" style="left:444px;top:1585px;background:linear-gradient(170deg,#7a9a4a,#b08a5a 50%,#8a5a3a)"></div>
  <div class="project" role="img" aria-label="Stilted lodge on red earth" style="left:776px;top:1585px;background:linear-gradient(180deg,#8ab4e0,#c07a50 65%,#b0502a)"></div>
  <div class="project" role="img" aria-label="Wooden cabin on a green lawn" style="left:112px;top:1796px;background:linear-gradient(170deg,#5a7a3a,#7a5a3a 50%,#6aa03a)"></div>
  <div class="project" role="img" aria-label="Lakeside lodge with snowy mountain" style="left:444px;top:1796px;background:linear-gradient(180deg,#9ab8d8,#6a7a7a 45%,#3a4a3a)"></div>
  <div class="project" role="img" aria-label="Boardwalk between thatched chalets" style="left:776px;top:1796px;background:linear-gradient(170deg,#8a7a50,#4a3a2a 60%,#2a2a20)"></div>
</section>

<section class="news">
  <h2 class="section-title" style="top:2132px">Latest News</h2>
  <div class="news-card" style="left:-10px;top:2248px;width:150px;height:155px"><div role="img" aria-label="Thatched lodge on a hill" style="background:linear-gradient(180deg,#a8c4e0,#7a6a4a)"></div></div>
  <div class="news-card" style="left:198px;top:2245px;width:434px;height:325px"><div role="img" aria-label="Thatched lodges among rocky hills" style="background:linear-gradient(180deg,#5a9ae0,#a8c0d8 30%,#8a7a5a 60%,#a09080)"></div></div>
  <div class="news-card" style="left:1060px;top:2252px;width:160px;height:155px"><div role="img" aria-label="Red roofed lodge among palms" style="background:linear-gradient(180deg,#b0c8e0,#4a7a3a)"></div></div>
  <h3 class="news-heading">Sed ut perspiciatis unde</h3>
  <p class="news-text">Lorem ipsum dolor sit amet, consectetur adipiscing elit, sed do eiusmod tempor incididunt ut labore et dolore magna aliqua. Ut enim ad minim veniam, quis nostrud exercitation ullamco laboris nisi ut aliquip ex ea commodo consequat. Duis aute irure dolor in reprehenderit in voluptate velit esse cillum dolore eu fugiat nulla pariatur.</p>
  <div class="btn" style="left:683px;top:2507px;width:175px;height:45px;font-size:16px">View More</div>
  <svg class="arrow" style="left:49px;top:2430px" viewBox="0 0 26 26"><circle cx="13" cy="13" r="11.5" fill="none" stroke="#555" stroke-width="1.5"/><polyline points="15,8 10,13 15,18" fill="none" stroke="#555" stroke-width="1.8"/></svg>
  <svg class="arrow" style="left:1117px;top:2430px" viewBox="0 0 26 26"><circle cx="13" cy="13" r="11.5" fill="none" stroke="var(--red)" stroke-width="1.5"/><polyline points="11,8 16,13 11,18" fill="none" stroke="var(--red)" stroke-width="1.8"/></svg>
</section>

<section class="testimonials">
  <h2 class="section-title" style="top:2718px">Testimonials</h2>
  <div class="quote" style="left:118px">Lorem ipsum dolor sit amet, consectetur adipiscing elit, sed do eiusmod tempor incididunt ut labore et dolore magna aliqua.</div>
  <div class="quote" style="left:450px">Lorem ipsum dolor sit amet, consectetur adipiscing elit, sed do eiusmod tempor incididunt ut labore et dolore magna aliqua.</div>
  <div class="quote" style="left:785px">Lorem ipsum dolor sit amet, consectetur adipiscing elit, sed do eiusmod tempor incididunt ut labore et dolore magna aliqua.</div>
  <div class="avatar" role="img" aria-label="Portrait of Lena Marsh" style="left:222px;background:linear-gradient(180deg,#6a4a3a,#c8a090)"></div>
  <div class="avatar" role="img" aria-label="Portrait of Tom Reyes" style="left:554px;background:linear-gradient(180deg,#8a5a3a,#d0a890)"></div>
  <div class="avatar" role="img" aria-label="Portrait of Omar Dell" style="left:889px;background:linear-gradient(180deg,#c0c8d0,#3a4a6a)"></div>
  <div class="person" style="left:118px"><div class="name">Lena Marsh</div><div class="place">USA</div><div class="stars">★★★★★</div></div>
  <div class="person" style="left:450px"><div class="name">Tom Reyes</div><div class="place">USA</div><div class="stars">★★★★★</div></div>
  <div class="person" style="left:785px"><div class="name">Omar Dell</div><div class="place">USA</div><div class="stars">★★★★★</div></div>
</section>

<footer class="footer-wrap">
  <svg class="footer" width="1200" height="458" viewBox="0 0 1200 458">
    <polygon points="0,88 800,8 1200,84 1200,458 0,458" fill="var(--black)"/>
    <polyline points="0,88 800,8 1200,84" fill="none" stroke="var(--red)" stroke-width="4"/>
  </svg>
  <div class="footer-brand">KPV<br>Construction</div>

  <div class="f-head" style="left:445px">Newsletter</div>
  <p class="f-text" style="left:445px;top:3478px;width:180px">Subscribe to us to get and receive the latest news, sales and updates.</p>
  <p class="f-text" style="left:445px;top:3556px;font-size:11px">Email Address:</p>
  <div class="abs" style="left:445px;top:3580px;width:165px;height:1px;background:#777"></div>
  <div class="btn" style="left:445px;top:3600px;width:112px;height:37px;font-size:14px">Sign Up</div>

  <div class="f-head" style="left:695px">Links</div>
  <ul class="f-links"><li>Home</li><li>About Us</li><li>Projects</li><li>Testimonials</li><li>Contact</li></ul>

  <div class="f-head" style="left:860px">Contact Us</div>
  <svg class="abs" style="left:858px;top:3484px" width="18" height="24" viewBox="0 0 18 24"><path d="M9 1C4.6 1 1.5 4.2 1.5 8.3 1.5 14 9 22.5 9 22.5S16.5 14 16.5 8.3C16.5 4.2 13.4 1 9 1Z" fill="none" stroke="#fff" stroke-width="1.5"/><circle cx="9" cy="8.5" r="2.8" fill="none" stroke="#fff" stroke-width="1.5"/></svg>
  <p class="f-text" style="left:897px;top:3478px;font-size:13px">412 North Hill Road,<br>Sample City, USA</p>
  <svg class="abs" style="left:858px;top:3536px" width="22" height="22" viewBox="0 0 22 22"><path d="M5 2l4 5-2.5 2.5c1.2 2.6 3.4 4.8 6 6L15 13l5 4-2 3c-8 0-16-8-16-16Z" fill="none" stroke="#fff" stroke-width="1.5" stroke-linejoin="round"/></svg>
  <p class="f-text" style="left:900px;top:3538px;font-size:13px">(555) 014 7788</p>
  <svg class="abs" style="left:858px;top:3596px" width="26" height="18" viewBox="0 0 26 18"><rect x="1" y="1" width="24" height="16" fill="none" stroke="#fff" stroke-width="1.5"/><polyline points="1,1 13,10 25,1" fill="none" stroke="#fff" stroke-width="1.5"/></svg>
  <p class="f-text" style="left:905px;top:3595px;font-size:13px">info@kpvconstruction.com</p>

  <p class="f-text" style="left:115px;top:3697px;font-size:12px">Copyright © 2019 All Rights are Reserved.</p>
  <div class="social" style="left:925px"></div>
  <div class="social on" style="left:958px"></div>
  <div class="social" style="left:998px"></div>
  <div class="social" style="left:1034px"></div>
</footer>

</body>
</html>
```